Verpackungen für ein Deo
Zielgruppe
ZONK BR... ähm MAU! Wir benötigen ein Design für die Verpackung unseres Case. Statt einer typischen Schachtel, wollen wir ein Label um unser Case herumwickeln, das einerseits unser Case schützt, andererseits auf unser REFILL System aufmerksam macht und im Inneren auch erklärt, wie das Produkt funktioniert und unsere Story erzählt. Wir wollen unnötige Verpackung vermeiden - also am besten besteht das Label/die Verpackung aus einem Stück. Auch soll die Farbe des Cases gut sichtbar sein. Wir haben bereits ein grobes Schnittmuster angehängt, wie so ein Label aussehen könnte. Man muss sich aber nicht daran halten. Gerne eigene Ideen einfließen lassen. Unser Case ist ca. 8,3cm hoch und hat einen Durchmesser von ca. 4,6cm
Es handelt sich dabei um ein Refill Deo. Nähere Infos findet ihr auf unserer Homepage. https://www.zonk-mau.example/pages/refill-deo
Unsere Marke tritt jung, modern und auffällig auf.
Wir sind zwar nachhaltig, aber keineswegs langweilig.
Unsere Cases gibt es in sportlichen Farben. Wir wollen Menschen dabei unterstützen selbstsicher zu sein und lieben 'dad-jokes' Du darfst also auch laut sein.
Also tobe dich aus! Wir sind auf deine Ideen gespannt!
Aufgabenstellung
1.Müssen Sie nur die Vorderseite des Etiketts?
-> Das Etikett soll von Außen und Innen designed werden. Außen soll ganz klar sichtbar sein, dass es sich um ein Case für unser Refill Deo handelt. Innen wollen wir zeigen wie es funktioniert und kurz auf unsere Story aufmerksam machen. Siehe Anhang (Was muss drauf sein)
2. Wie groß ist das Fenster, das für den Druck der Chargennummer belassen werden soll? Und gibt es eine vorgeschriebene Stelle auf dem Etikett, an der sie angebracht werden muss?
-> Da das Case ohne Refill verkauft wird benötigen wir keine Chargennummer.
3. In der Aufgabe, die auf dem Etikett platziert werden muss, ist kein QR und EAN-Code enthalten. Soll ich nur die Code-Visualisierung einfügen oder wird der Code später zur Verfügung gestellt?
-> Genau. Code wird später zur Verfügung gestellt, bzw. bekommt jede Case Farbe einen eigenen Ean Code. Muss Mindestens 3x1,5cm groß sein
4.Es gibt kein NON GMO-Zeichen in der Aufgabe, das auf dem Etikett platziert werden muss. Soll ich nur die Code-Visualisierung platzieren oder wird das Schild später bereitgestellt?
-> wird nicht benötigt
5. Die Aufgabe enthält keine Zutaten- und Nährwerttabelle. Könntest du sie zum Wettbewerb hinzufügen?
-> Nicht benötigt. Das ist die Verpackung nur für das Case. Das Deo Refill wird seperat angeboten
6.Auf dem Etikett sollte Made in Germany(Österreich) stehen?
7. Welche Farbe und welche Schriftart möchten Sie verwenden? Dies ist für einen Designer sehr wichtig zu wissen.
-> Da unsere Cases sehr bunt sind, kann das Etikett schlicht gestaltet sein. Unsere CI Schriftart ist ROBOTO
-> CI Farben:
LIME / Neon Gelb
PANTONE 388 C
FARBWERTE:
RGB 224 231 34
HEX/HTML E0E722
CMYK 11 0 91 0
PINK / Neon Pin..

```html
<!DOCTYPE html>
<html lang="de">
<head>
<meta charset="utf-8">
<title>ZONK MAU! – Refill Deo Push Up Case Etikett</title>
<link rel="stylesheet" href="https://fonts.googleapis.com/css2?family=Roboto:wght@400;700;900&family=Roboto+Condensed:wght@700&display=swap">
<style>
  :root {
    --bg: #ececec;
    --charcoal: #2c2c2e;
    --magenta: #c8237a;
    --white: #ffffff;
    --soft-pink: #f3b8d6;
  }
  * { margin: 0; padding: 0; box-sizing: border-box; }
  html, body { width: 1200px; height: 675px; overflow: hidden; background: var(--bg); }
  .canvas {
    position: relative; width: 1200px; height: 675px;
    display: flex; align-items: center; justify-content: center;
    font-family: "Roboto", sans-serif;
  }
  .label {
    display: flex; width: 1000px; height: 380px;
    background: var(--charcoal);
  }
  .panel { position: relative; height: 100%; }
  .panel-info { width: 220px; padding: 40px 26px; color: var(--white); }
  .info-text {
    font-size: 12px; line-height: 1.6; text-transform: uppercase;
    letter-spacing: 0.04em; font-weight: 700;
  }
  .strip {
    width: 90px; background: var(--magenta);
    display: flex; align-items: center; justify-content: center;
  }
  .strip-title {
    font-family: "Roboto Condensed", sans-serif; font-weight: 700;
    font-size: 40px; letter-spacing: 0.06em; color: var(--white);
    writing-mode: vertical-rl; transform: rotate(180deg); white-space: nowrap;
  }
  .panel-front { width: 340px; }
  .front-shape { position: absolute; inset: 0 0 auto 0; width: 100%; height: 250px; }
  .brand-name {
    position: absolute; top: 48px; left: 0; width: 100%;
    text-align: center; color: var(--white);
    font-weight: 900; font-size: 62px; line-height: 1.05; letter-spacing: 0.01em;
  }
  .product-block {
    position: absolute; top: 262px; left: 0; width: 100%; text-align: center; color: var(--white);
  }
  .product-name {
    font-family: "Roboto Condensed", sans-serif; font-weight: 700; font-size: 20px;
    letter-spacing: 0.03em; display: inline-block; padding: 0 8px 6px;
    border-bottom: 3px solid var(--magenta);
  }
  .product-note {
    margin: 12px auto 0; width: 220px; font-size: 11px; font-weight: 700;
    line-height: 1.45; text-transform: uppercase; color: var(--soft-pink);
  }
  .panel-back { width: 260px; }
</style>
</head>
<body>
<main class="canvas">
  <section class="label" aria-label="Etikett Push Up Case">
    <div class="panel panel-info">
      <p class="info-text">Einfach Kartusche rein, hochdrehen, fertig. Weniger Müll, mehr Selbstvertrauen. Nachfüllen statt wegwerfen.</p>
    </div>
    <div class="strip"><span class="strip-title">REFILL DEO</span></div>
    <div class="panel panel-front">
      <svg class="front-shape" viewBox="0 0 340 250" preserveAspectRatio="none" aria-hidden="true">
        <polygon points="20,0 320,0 320,190 170,250 20,190" fill="var(--magenta)"/>
      </svg>
      <h1 class="brand-name">ZONK<br>MAU!</h1>
      <div class="product-block">
        <h2 class="product-name">PUSH UP CASE</h2>
        <p class="product-note">Case für den Einsatz von Refill Deo Kartuschen von Zonk Mau</p>
      </div>
    </div>
    <div class="strip"><span class="strip-title">REFILL DEO</span></div>
    <div class="panel panel-back"></div>
  </section>
</main>
</body>
</html>
```